Oven Cleaning Business owner needs business card design

Hi there,
Would like for a business card to be designed for myself, the owner of a professional oven cleaning business on the Sunshine Coast.
Would like it to look sleek, and modern-ish. Bit creative is encouraged too.
Include following:
Name/title: Corin ter Haghe, Owner
Phone number: 1300 482 916
Email: info@hearthshinecrew.com.au
Website: www.hearthshinecrew.com.au

```html
<!DOCTYPE html>
<html lang="en">
<head>
<meta charset="utf-8">
<title>Hearthshine Crew – Business Card</title>
<link href="https://fonts.googleapis.com/css2?family=Exo+2:wght@300;400;700;800&display=swap" rel="stylesheet">
<style>
  :root {
    --bg: #2a2a2c;
    --card-white: #ffffff;
    --teal: #1fd6d9;
    --teal-deep: #14bfc3;
    --ink: #111214;
    --rule: #9a9a9a;
  }
  * { margin: 0; padding: 0; box-sizing: border-box; }
  html, body { width: 1200px; height: 1108px; overflow: hidden; }
  body {
    background: var(--bg);
    font-family: "Exo 2", sans-serif;
    position: relative;
  }
  .card {
    position: absolute;
    top: 229px;
    width: 400px;
    height: 650px;
    border-radius: 22px;
    overflow: hidden;
  }
  .card--front { left: 160px; background: var(--card-white); }
  .card--back { left: 640px; background: var(--teal); }

  .brand {
    position: absolute;
    top: 170px;
    left: 0; right: 0;
    text-align: center;
  }
  .brand__mark {
    display: block;
    width: 56px; height: 56px;
    margin: 0 auto 22px;
    border-radius: 50%;
    background: var(--teal);
  }
  .brand__name {
    font-weight: 800;
    font-size: 40px;
    line-height: 1.05;
    letter-spacing: 2px;
    color: var(--ink);
    text-transform: uppercase;
  }

  .person {
    position: absolute;
    top: 390px;
    left: 0; right: 0;
    text-align: center;
  }
  .person__name {
    font-weight: 700;
    font-size: 26px;
    color: var(--ink);
    text-transform: uppercase;
    letter-spacing: 0.5px;
  }
  .person__title {
    font-weight: 300;
    font-size: 18px;
    color: var(--teal);
    letter-spacing: 1px;
    text-transform: uppercase;
    margin-top: 2px;
  }

  .contact-icons {
    position: absolute;
    top: 470px;
    left: 60px; right: 60px;
    display: flex;
    align-items: center;
    gap: 6px;
  }
  .contact-icons__rule { flex: 1; height: 1px; background: var(--rule); }
  .contact-icons__icon {
    width: 30px; height: 30px;
    border-radius: 4px;
    background: var(--teal);
    display: flex; align-items: center; justify-content: center;
  }
  .contact-icons__icon svg { width: 18px; height: 18px; }

  .contact-list {
    position: absolute;
    top: 522px;
    left: 0; right: 0;
    text-align: center;
    list-style: none;
    font-weight: 400;
    font-size: 17px;
    line-height: 1.6;
    color: var(--ink);
  }

  .back-pattern {
    position: absolute;
    inset: 0;
    background: linear-gradient(160deg, #2ae3e6 0%, var(--teal) 50%, var(--teal-deep) 100%);
  }
  .back-mark {
    position: absolute;
    left: 236px;
    top: 470px;
    width: 46px; height: 46px;
    border-radius: 50%;
    background: var(--card-white);
  }
</style>
</head>
<body>

<section class="card card--front" aria-label="Business card front">
  <div class="brand">
    <span class="brand__mark"></span>
    <div class="brand__name">Hearthshine<br>Crew</div>
  </div>

  <div class="person">
    <div class="person__name">Corin ter Haghe</div>
    <div class="person__title">Owner</div>
  </div>

  <div class="contact-icons">
    <span class="contact-icons__rule"></span>
    <span class="contact-icons__icon" aria-label="Phone">
      <svg viewBox="0 0 24 24" fill="none" stroke="#fff" stroke-width="2"><path d="M5 4h4l2 5-2.5 1.5a11 11 0 0 0 5 5L15 13l5 2v4a2 2 0 0 1-2 2A16 16 0 0 1 3 6a2 2 0 0 1 2-2z"/></svg>
    </span>
    <span class="contact-icons__icon" aria-label="Email">
      <svg viewBox="0 0 24 24" fill="none" stroke="#fff" stroke-width="2"><rect x="3" y="5" width="18" height="14"/><path d="M3 5l9 8 9-8"/></svg>
    </span>
    <span class="contact-icons__icon" aria-label="Website">
      <svg viewBox="0 0 24 24" fill="none" stroke="#fff" stroke-width="2"><circle cx="12" cy="12" r="9"/><path d="M3 12h18M12 3c3 3 3 15 0 18M12 3c-3 3-3 15 0 18"/></svg>
    </span>
    <span class="contact-icons__rule"></span>
  </div>

  <ul class="contact-list">
    <li>1300 482 916</li>
    <li>info@hearthshinecrew.com.au</li>
    <li>www.hearthshinecrew.com.au</li>
  </ul>
</section>

<section class="card card--back" aria-label="Business card back">
  <div class="back-pattern" role="img" aria-label="Repeating tone-on-tone embossed brand pattern on teal"></div>
  <span class="back-mark"></span>
</section>

</body>
</html>
```